Torvel, Inc. new buisness cards - brand guide included

We need new business cards. SLEAK SIMPLE FINANCE. They must include a place for NAME, TITLE, CELL, OFFICE PHONE, EMAIL. they also must include our services across the bottom. AIR, OCEAN, FTL, LTL, EXPRESS. for reference this will be being handed to some of the most prestigious shipping companies in a america.

Target Market(s)

Finance and corporate

Contact Information for Business Card

We need new business cards. SLEAK SIMPLE FINANCE. They must include a place for NAME, TITLE, CELL, OFFICE PHONE, EMAIL. they also must include our services across the bottom. AIR, OCEAN, FTL, LTL, EXPRESS.

Requirements
Must have
• We need new business cards. SLEAK SIMPLE FINANCE. They must include a place for NAME, TITLE, CELL, OFFICE PHONE, EMAIL. they also must include our services across the bottom. AIR, OCEAN, FTL, LTL, EXPRESS.
Nice to have
• USE THE COLORS AND LOGO IN THE BRAND GUIDE :)

```html
<!DOCTYPE html>
<html lang="en">
<head>
<meta charset="UTF-8">
<title>Torvel, Inc. — Business Card</title>
<link rel="stylesheet" href="https://fonts.googleapis.com/css2?family=Montserrat:wght@400;500;700&display=swap">
<style>
  :root {
    --stage: #2a2a2a;
    --gold: #c8b999;
    --gold-icon: #bfa97f;
    --paper: #ffffff;
    --ink: #262626;
    --ink-soft: #3a3a3a;
    --white: #ffffff;
  }
  * { margin: 0; padding: 0; box-sizing: border-box; }
  html, body {
    width: 1200px;
    height: 875px;
    overflow: hidden;
    background: var(--stage);
    font-family: "Montserrat", sans-serif;
  }
  .canvas {
    width: 1200px;
    height: 875px;
    display: flex;
    flex-direction: column;
    align-items: center;
    justify-content: center;
    gap: 48px;
  }
  .card {
    width: 640px;
    height: 366px;
    border-radius: 26px;
    position: relative;
    overflow: hidden;
  }

  /* Front */
  .card-front {
    background: var(--gold);
    color: var(--white);
    display: flex;
    flex-direction: column;
    align-items: center;
    justify-content: center;
  }
  .front-brand {
    font-size: 82px;
    font-weight: 500;
    letter-spacing: 10px;
    line-height: 1;
    margin-top: 20px;
  }
  .front-services {
    margin-top: 46px;
    font-size: 13px;
    font-weight: 400;
    letter-spacing: 1.6px;
  }

  /* Back */
  .card-back {
    background: var(--paper);
    color: var(--ink);
    display: flex;
    align-items: center;
    padding-left: 70px;
  }
  .back-brand {
    font-size: 46px;
    font-weight: 500;
    letter-spacing: 5px;
    color: var(--ink);
    width: 236px;
  }
  .divider {
    width: 1.5px;
    height: 150px;
    background: var(--ink);
    margin: 0 22px 0 8px;
  }
  .contact { display: flex; flex-direction: column; }
  .contact-name {
    font-size: 20px;
    font-weight: 700;
    color: var(--ink);
  }
  .contact-title {
    font-size: 13px;
    font-weight: 400;
    color: var(--ink-soft);
    margin-bottom: 14px;
  }
  .contact-line {
    display: flex;
    align-items: center;
    gap: 12px;
    font-size: 14px;
    color: var(--ink);
    line-height: 1.75;
  }
  .contact-line svg { width: 13px; height: 13px; fill: var(--gold-icon); flex: none; }
</style>
</head>
<body>
<main class="canvas">
  <section class="card card-front">
    <div class="front-brand">TORVEL</div>
    <div class="front-services">AIR. OCEAN. FTL. LTL. EXPRESS.</div>
  </section>

  <section class="card card-back">
    <div class="back-brand">TORVEL</div>
    <div class="divider"></div>
    <div class="contact">
      <div class="contact-name">Dario Feldt</div>
      <div class="contact-title">Managing Director</div>
      <div class="contact-line">
        <svg viewBox="0 0 24 24" aria-hidden="true"><path d="M6.6 10.8a15.1 15.1 0 0 0 6.6 6.6l2.2-2.2a1 1 0 0 1 1-.25 11.4 11.4 0 0 0 3.6.57 1 1 0 0 1 1 1V20a1 1 0 0 1-1 1A17 17 0 0 1 3 4a1 1 0 0 1 1-1h3.5a1 1 0 0 1 1 1c0 1.25.2 2.45.57 3.57a1 1 0 0 1-.25 1z"/></svg>
        <span>310.555.0142</span>
      </div>
      <div class="contact-line">
        <svg viewBox="0 0 24 24" aria-hidden="true"><path d="M3 8c0-2 4-4 9-4s9 2 9 4v2h-5V8H8v2H3z"/><path d="M6 12h12l2 8H4z"/></svg>
        <span>310.555.0187</span>
      </div>
      <div class="contact-line">
        <svg viewBox="0 0 24 24" aria-hidden="true"><path d="M2 5h20v14H2z M3.5 6.5 12 13l8.5-6.5" /></svg>
        <span>name@torvelfreight.com</span>
      </div>
    </div>
  </section>
</main>
</body>
</html>
```